Design Our Holiday Magic Coupon

Purpose - The purpose of this project is to create a festive, uplifting, and visually engaging physical coupon that will be mailed to our existing community and warm leads.
The intent is twofold: first, to spark delight and connection by offering a tangible, personal touch during the holiday season; and second, to encourage customers to explore and purchase our programs as they prepare for a strong start to 2026. This mailer is designed to re-engage past buyers, inspire current participants, and gently invite new momentum into their practice through a simple, friendly offer.

Project Description + Scope

This project includes the design and production of a printed coupon ( card format) featuring a 20% discount on purchases of $79 or more. The copy should feel warm, clear, and celebratory without urgency or pressure.

The front of the card will include the headline (“Live Your Best 2026”), bold discount information, and the coupon code JOLLYDAY20. The back will include a short message reinforcing the tone of possibility and ease, plus simple redemption instructions and the expiry date: December 31, 2025. Deliverables include print-ready artwork, color selection aligned with KH brand style.

one side
LIVE YOUR BEST 2026
Enjoy 20% OFF when you buy $79 or more.
Use code: JOLLYDAY20
Redeem until end of day December 31, 2025.

Back side - Move with clarity.
Heal with intelligence.
Lead with ease.
Thank you for being part of Kinetic Harmony.
Lots of love, Marla and the whole of Team Marla

Target Market(s)

yoga teachers, yoga lovers, mostly over 50 years, women

Font styles to use
Other font styles liked:
• see attached for feel

Colors
0054AA
0677BA
7BADD7
CADEEF
E8F1F8
0094D4
00A9DD
6FCCEA
C7EBF8
E9F6FB
00AB8E
00BBA5
67D7C9
C6EFE9
E9F9F6
EB3D1F
EC4F4E
F09395
F8D3D4
FCEDEE

Requirements
Nice to have
• see attached

```html
<!DOCTYPE html>
<html lang="en">
<head>
<meta charset="utf-8">
<title>Kinetic Harmony Holiday Coupon</title>
<link rel="stylesheet" href="https://fonts.googleapis.com/css2?family=Fira+Sans+Condensed:ital,wght@0,400;0,600;0,700;1,400;1,700&family=Fira+Sans+Extra+Condensed:wght@700&display=swap">
<style>
  :root {
    --page-bg-top: #d2d2d2;
    --page-bg-bottom: #ffffff;
    --ink-black: #000000;
    --amber: #c47a31;
    --amber-light: #cf8a3c;
    --amber-dark: #b96f2a;
    --sun-yellow: #fbb040;
    --paper-white: #ffffff;
  }
  * { margin: 0; padding: 0; box-sizing: border-box; }
  html, body {
    width: 1051px;
    height: 1200px;
    overflow: hidden;
  }
  body {
    background: linear-gradient(180deg, var(--page-bg-top) 0%, var(--page-bg-bottom) 100%);
    font-family: "Fira Sans Condensed", "Arial Narrow", sans-serif;
    position: relative;
  }
  .coupon-card {
    position: absolute;
    left: 100px;
    width: 851px;
    height: 531px;
    overflow: hidden;
    box-shadow: 6px 8px 10px rgba(0, 0, 0, 0.45);
  }
  .coupon-front { top: 53px; }
  .coupon-back { top: 617px; }

  .texture-field {
    position: absolute;
    inset: 0;
    background:
      radial-gradient(ellipse at 92% 30%, var(--amber-light) 0%, transparent 45%),
      radial-gradient(ellipse at 15% 20%, var(--amber-light) 0%, transparent 40%),
      linear-gradient(180deg, var(--amber) 0%, var(--amber-dark) 100%);
  }
  .card-shape {
    position: absolute;
    inset: 0;
    width: 100%;
    height: 100%;
  }

  /* Front */
  .headline-vertical {
    position: absolute;
    left: 172px;
    top: 265px;
    transform: translate(-50%, -50%) rotate(-90deg);
    white-space: nowrap;
    font-family: "Fira Sans Extra Condensed", "Arial Narrow", sans-serif;
    font-weight: 700;
    font-size: 104px;
    line-height: 88px;
    color: var(--sun-yellow);
    text-transform: uppercase;
    letter-spacing: 0;
  }
  .offer-block {
    position: absolute;
    left: 344px;
    right: 0;
    top: 196px;
    text-align: center;
    color: var(--paper-white);
    font-size: 23px;
  }
  .offer-block p { line-height: 53px; height: 53px; }
  .offer-block strong { font-weight: 700; }
  .offer-code { font-weight: 700; }
  .offer-expiry { font-style: italic; }

  /* Back */
  .message-block {
    position: absolute;
    left: 0;
    right: 0;
    top: 88px;
    text-align: center;
    color: var(--paper-white);
  }
  .message-lead {
    font-weight: 700;
    font-size: 60px;
    line-height: 76px;
    letter-spacing: -0.5px;
  }
  .message-line {
    font-size: 23px;
    line-height: 52px;
  }
  .signoff-block {
    position: absolute;
    left: 0;
    right: 0;
    top: 396px;
    text-align: center;
    color: var(--sun-yellow);
    font-size: 23px;
    line-height: 34px;
  }
  .signoff-thanks { font-weight: 700; font-style: italic; }
</style>
</head>
<body>

  <section class="coupon-card coupon-front" aria-label="Coupon front">
    <div class="texture-field" role="img" aria-label="Distressed amber grunge texture"></div>
    <svg class="card-shape" viewBox="0 0 851 531" aria-hidden="true">
      <path fill="var(--ink-black)" stroke="var(--paper-white)" stroke-width="2.5"
        d="M0 0 L344 0
           q 12 8.3 0 16.6 q -12 8.3 0 16.6
           q 12 8.3 0 16.6 q -12 8.3 0 16.6
           q 12 8.3 0 16.6 q -12 8.3 0 16.6
           q 12 8.3 0 16.6 q -12 8.3 0 16.6
           q 12 8.3 0 16.6 q -12 8.3 0 16.6
           q 12 8.3 0 16.6 q -12 8.3 0 16.6
           q 12 8.3 0 16.6 q -12 8.3 0 16.6
           q 12 8.3 0 16.6 q -12 8.3 0 16.6
           q 12 8.3 0 16.6 q -12 8.3 0 16.6
           q 12 8.3 0 16.6 q -12 8.3 0 16.6
           q 12 8.3 0 16.6 q -12 8.3 0 16.6
           q 12 8.3 0 16.6 q -12 8.3 0 16.6
           q 12 8.3 0 16.6 q -12 8.3 0 16.6
           q 12 8.3 0 16.6 q -12 8.3 0 16.6
           q 12 8.3 0 16.6 q -12 8.3 0 16.6
           q 12 8.3 0 16.6 q -12 8.3 0 16.6
           L0 531 Z"/>
    </svg>
    <h1 class="headline-vertical">Live Your<br>Best 2026</h1>
    <div class="offer-block">
      <p class="offer-terms">Enjoy <strong>20% OFF</strong> when you buy <strong>$79</strong> or more.</p>
      <p class="offer-code">Use code: JOLLYDAY20</p>
      <p class="offer-expiry">Redeem until end of day December 31, 2025.</p>
    </div>
  </section>

  <section class="coupon-card coupon-back" aria-label="Coupon back">
    <div class="texture-field" role="img" aria-label="Distressed amber grunge texture"></div>
    <svg class="card-shape" viewBox="0 0 851 531" aria-hidden="true">
      <path fill="var(--ink-black)" stroke="var(--paper-white)" stroke-width="2.5"
        d="M0 327
           q 9.7 -12 19.35 0 q 9.7 12 19.35 0
           q 9.7 -12 19.35 0 q 9.7 12 19.35 0
           q 9.7 -12 19.35 0 q 9.7 12 19.35 0
           q 9.7 -12 19.35 0 q 9.7 12 19.35 0
           q 9.7 -12 19.35 0 q 9.7 12 19.35 0
           q 9.7 -12 19.35 0 q 9.7 12 19.35 0
           q 9.7 -12 19.35 0 q 9.7 12 19.35 0
           q 9.7 -12 19.35 0 q 9.7 12 19.35 0
           q 9.7 -12 19.35 0 q 9.7 12 19.35 0
           q 9.7 -12 19.35 0 q 9.7 12 19.35 0
           q 9.7 -12 19.35 0 q 9.7 12 19.35 0
           q 9.7 -12 19.35 0 q 9.7 12 19.35 0
           q 9.7 -12 19.35 0 q 9.7 12 19.35 0
           q 9.7 -12 19.35 0 q 9.7 12 19.35 0
           q 9.7 -12 19.35 0 q 9.7 12 19.35 0
           q 9.7 -12 19.35 0 q 9.7 12 19.35 0
           q 9.7 -12 19.35 0 q 9.7 12 19.35 0
           q 9.7 -12 19.35 0 q 9.7 12 19.35 0
           q 9.7 -12 19.35 0 q 9.7 12 19.35 0
           q 9.7 -12 19.35 0 q 9.7 12 19.35 0
           q 9.7 -12 19.35 0 q 9.7 12 19.35 0
           q 9.7 -12 19.35 0 q 9.7 12 19.35 0
           L851 531 L0 531 Z"/>
    </svg>
    <div class="message-block">
      <h2 class="message-lead">Move with clarity.</h2>
      <p class="message-line">Heal with intelligence.</p>
      <p class="message-line">Lead with ease.</p>
    </div>
    <div class="signoff-block">
      <p class="signoff-thanks">Thank you for being part of Kinetic Harmony.</p>
      <p class="signoff-love">Lots of love, Marla and the whole of Team Marla</p>
    </div>
  </section>

</body>
</html>
```